Kinsmen Crest Beard Oil Label for 1oz dropper bottle

Create a label for a 1oz beard oil dropper bottle. The label is 1.5 inches tall and 2.75 inches wide. Our logo is listed in the brief so please use it but it doesnt have to be that prominent. BEARD OIL is the most important verbiage. We like elements of all the attached images but we want our own look and feel.

Target Market(s)

Men with beards

Requirements
Must have
• Kinsmen Crest Logo, BEARD OIL, Flavor (Tobacco Vanilla)

Ingredients
Fractionated Coconut Oil (MCT)
Golden Jojoba Oil
Hemp Seed Oil
Tea Tree Essential Oil
Orange Bitter Essential Oil
Peppermint Supreme Essential Oil
Tallow Aromas
DYE FREE

Directions:
Directions: apply 3-6 drops into your hand...rub oil into hands and apply directly onto beard. For best results massage into skin under beard area and work oil out towards beard. Discontinue use if skin becomes irritated.

100% MADE IN THE USA (American Flag 1 color)
Veteran Owned Co.
Nice to have
• Labels can change color with each flavor or a ring can change color to show flavor.

```html
<!DOCTYPE html>
<html lang="en">
<head>
<meta charset="utf-8">
<title>Kinsmen Crest Beard Oil Label</title>
<link href="https://fonts.googleapis.com/css2?family=Oswald:wght@300;400&family=Rye&display=swap" rel="stylesheet">
<style>
  :root {
    --paper: #ffffff;
    --label-edge: #e3e1d5;
    --tan: #d1c9a1;
    --steel: #426b7a;
    --charcoal: #231f20;
    --cream: #e4e5d9;
    --ember: #e05a2e;
    --ink: #231f20;
  }
  * { margin: 0; padding: 0; box-sizing: border-box; }
  html, body { width: 1200px; height: 1200px; overflow: hidden; background: var(--paper); }
  .canvas { position: relative; width: 1200px; height: 1200px; }

  .label {
    position: absolute; left: 51px; top: 301px; width: 1104px; height: 608px;
    background: var(--label-edge);
    box-shadow: 2px 3px 4px rgba(0,0,0,.35);
    overflow: hidden;
  }
  .label__steel {
    position: absolute; left: 14px; right: 14px; top: 6px; bottom: 6px;
    background: var(--steel);
  }
  .label__header {
    position: absolute; left: 14px; right: 14px; top: 17px; height: 154px;
    background: var(--tan);
    display: flex; align-items: center; justify-content: center;
    padding-top: 30px;
  }
  .brand {
    display: flex; align-items: center; gap: 12px;
    font-family: "Rye", serif; font-size: 34px; color: var(--ink); letter-spacing: 1px;
  }
  .brand__dot { width: 12px; height: 12px; border-radius: 50%; background: var(--ink); }

  .label__panel {
    position: absolute; left: 14px; right: 14px; top: 192px; height: 401px;
    background: var(--charcoal);
  }

  .ingredients, .directions, .footer-note, .volume {
    font-family: "Oswald", sans-serif; font-weight: 300; color: var(--cream);
  }
  .ingredients { position: absolute; left: 42px; top: 222px; }
  .ingredients h2 { font-weight: 300; font-size: 26px; line-height: 34px; }
  .ingredients li { list-style: none; font-size: 21px; line-height: 32.4px; white-space: nowrap; }

  .directions { position: absolute; left: 788px; top: 220px; width: 300px; }
  .directions h2 { font-weight: 300; font-size: 26px; line-height: 34px; }
  .directions p { font-size: 20px; line-height: 30.8px; white-space: nowrap; }

  .title {
    font-family: "Rye", serif; color: var(--cream);
    text-shadow: 2px 2px 0 var(--ember), 4px 4px 0 var(--ember);
    font-weight: 400;
  }
  .title__beard {
    position: absolute; left: 320px; top: 210px; width: 440px; text-align: center;
    font-size: 96px; line-height: 170px;
    transform: rotate(-6deg) scaleX(.86);
  }
  .title__oil {
    position: absolute; left: 519px; top: 375px; width: 160px; text-align: center;
    font-size: 62px; line-height: 76px;
    transform: scaleX(.86);
  }

  .flavor {
    position: absolute; left: 385px; top: 487px; width: 316px; height: 40px;
    background: var(--tan);
    clip-path: polygon(0 50%, 6% 0, 94% 0, 100% 50%, 94% 100%, 6% 100%);
    display: flex; align-items: center; justify-content: center;
    font-family: "Rye", serif; font-size: 19px; color: var(--ink); letter-spacing: 1px;
  }
  .volume { position: absolute; left: 443px; top: 555px; width: 200px; text-align: center; font-size: 21px; line-height: 28px; }

  .footer-note { position: absolute; left: 791px; top: 543px; font-size: 22px; line-height: 28px; white-space: nowrap; }
  .origin-badge { position: absolute; left: 949px; top: 461px; }
</style>
</head>
<body>
<div class="canvas">
  <section class="label">
    <div class="label__steel"></div>
    <header class="label__header">
      <div class="brand"><span class="brand__dot"></span>Kinsmen Crest</div>
    </header>
    <div class="label__panel"></div>

    <div class="ingredients">
      <h2>Ingredients:</h2>
      <ul>
        <li>Fractionated Coconut Oil (MCT)</li>
        <li>Golden Jojoba Oil</li>
        <li>Hemp Seed Oil</li>
        <li>Tea Tree Essential Oil</li>
        <li>Orange Bitter Essential Oil</li>
        <li>Peppermint Supreme Essential Oil</li>
        <li>Tallow Aromas</li>
        <li>DYE FREE</li>
      </ul>
    </div>

    <h1 class="title">
      <span class="title__beard">BEARD</span>
      <span class="title__oil">OIL</span>
    </h1>

    <div class="flavor">TOBACCO VANILLA</div>
    <div class="volume">1 fl oz. ( 30ml )</div>

    <div class="directions">
      <h2>Directions:</h2>
      <p>Directions: apply 3-6 drops into your<br>hand...rub oil into hands and apply<br>directly onto beard. For best results<br>massage into skin under beard area<br>and work oil out towards beard.<br>Discontinue use if skin becomes<br>irritated.</p>
    </div>

    <div class="footer-note">Veteran Owned Co.</div>
    <svg class="origin-badge" width="106" height="104" viewBox="0 0 106 104" role="img" aria-label="Made in USA badge">
      <rect x="0" y="0" width="106" height="104" fill="var(--cream)"/>
      <rect x="6" y="6" width="94" height="92" fill="var(--charcoal)"/>
    </svg>
  </section>
</div>
</body>
</html>
```